Wedding Company needs Brochure Design

FOR THIS PROJECT, WE ARE LOOKING FOR A BROCHURE. WHOEVER WE CHOOSE AS THE WINNING BROCHURE DESIGN WILL THEN DESIGN OUR WEBSITE AND BUSINESS CARD.

We're are looking to expand our brochure by making it a circle and adding 6 inside pages of information with a front and back cover. The pages will be as follows:

Front
About us
About us pictures
Wedding Planning
Wedding planning pictures
Lighting & Decor
Lighting & decor pictures
Back

We've uploaded a picture of our current brochure... so you can get an idea of what we've liked before. Please give us your creative input & design ideas. We've put together a "mock" brochure for you to take a look at as well. As you can see we need your help to properly lay out pictures so that the pages look full and the pictures pop and catches our clients attention.

A few words to describe our brochure would be "elegance", "class", "tasteful" and "colorful". We want to be able to portray that we are luxurious and innovative for the higher end brides and at the same time catering to the budget friendly brides.

Currently, we are waiting on a few pictures from the photographers and we are hoping to have them in a few days... In the meantime we've placed pictures we took from our phone as place holders.

Industry/Entity Type

Catering

```html
<!DOCTYPE html>
<html lang="en">
<head>
<meta charset="utf-8">
<title>Lighting &amp; Decor – Brochure Spread</title>
<link href="https://fonts.googleapis.com/css2?family=Great+Vibes&family=Arimo:wght@400&display=swap" rel="stylesheet">
<style>
  :root {
    --paper: #ffffff;
    --page-cream: #f7f2e4;
    --page-edge: #e6dcc4;
    --plum: #7b2f63;
    --plum-text: #7a3a6b;
    --gold: #c9a45e;
    --fold: #3a3a3a;
  }
  html, body {
    margin: 0;
    padding: 0;
    width: 1200px;
    height: 661px;
    overflow: hidden;
    background: var(--paper);
  }
  .spread { display: block; width: 1200px; height: 661px; }
  .page-shape { fill: var(--page-cream); stroke: var(--page-edge); stroke-width: 1; }
  .fold-line { stroke: var(--fold); stroke-width: 1.2; stroke-dasharray: 6 4; }
  .page-title {
    font-family: "Great Vibes", cursive;
    font-size: 52px;
    fill: var(--plum);
  }
  .body-copy {
    font-family: "Arimo", Arial, sans-serif;
    font-size: 10.4px;
    fill: var(--plum-text);
  }
  .service-list {
    font-family: "Arimo", Arial, sans-serif;
    font-size: 10.4px;
    fill: var(--plum-text);
  }
  .bullet { fill: var(--plum-text); }
  .frame-plum { fill: none; stroke: var(--plum); stroke-width: 4; }
  .frame-gold { fill: none; stroke: var(--gold); stroke-width: 4; }
</style>
</head>
<body>
<svg class="spread" viewBox="0 0 1000 551" xmlns="http://www.w3.org/2000/svg">
  <defs>
    <filter id="page-shadow" x="-10%" y="-10%" width="120%" height="120%">
      <feDropShadow dx="0" dy="2" stdDeviation="3" flood-color="#000" flood-opacity="0.25"/>
    </filter>
    <clipPath id="left-page-clip"><ellipse cx="276" cy="277" rx="232" ry="266"/></clipPath>
    <clipPath id="right-page-clip"><ellipse cx="737" cy="277" rx="240" ry="268"/></clipPath>

    <linearGradient id="tone-chandelier-hall" x1="0" y1="0" x2="0" y2="1">
      <stop offset="0" stop-color="#2f7c8a"/><stop offset="0.5" stop-color="#1c2c4a"/><stop offset="1" stop-color="#6a5a4a"/>
    </linearGradient>
    <linearGradient id="tone-candle-table" x1="0" y1="0" x2="1" y2="1">
      <stop offset="0" stop-color="#2a1a14"/><stop offset="0.5" stop-color="#8a5a3a"/><stop offset="1" stop-color="#e6a8b8"/>
    </linearGradient>
    <linearGradient id="tone-searchlight" x1="0" y1="0" x2="0" y2="1">
      <stop offset="0" stop-color="#1a2a5a"/><stop offset="0.6" stop-color="#243a7a"/><stop offset="1" stop-color="#5a3a2a"/>
    </linearGradient>
    <linearGradient id="tone-dessert-display" x1="0" y1="0" x2="0" y2="1">
      <stop offset="0" stop-color="#f2eef0"/><stop offset="0.6" stop-color="#e8c8d0"/><stop offset="1" stop-color="#c49a8a"/>
    </linearGradient>
    <linearGradient id="tone-purple-hall" x1="0" y1="0" x2="0" y2="1">
      <stop offset="0" stop-color="#6ab0c8"/><stop offset="0.5" stop-color="#5a3a8a"/><stop offset="1" stop-color="#2a1a4a"/>
    </linearGradient>
    <linearGradient id="tone-snowflake-room" x1="0" y1="0" x2="0" y2="1">
      <stop offset="0" stop-color="#4a5ab0"/><stop offset="0.6" stop-color="#3a2a6a"/><stop offset="1" stop-color="#6a5a8a"/>
    </linearGradient>
    <linearGradient id="tone-tent-gobo" x1="0" y1="0" x2="0" y2="1">
      <stop offset="0" stop-color="#4a6ad0"/><stop offset="0.5" stop-color="#8a4ac0"/><stop offset="1" stop-color="#1a1a3a"/>
    </linearGradient>
    <linearGradient id="tone-monogram-venue" x1="0" y1="0" x2="0" y2="1">
      <stop offset="0" stop-color="#1a1424"/><stop offset="0.5" stop-color="#8a6a3a"/><stop offset="1" stop-color="#3a2a2a"/>
    </linearGradient>
  </defs>

  <!-- Left page -->
  <g class="page page-left">
    <ellipse class="page-shape" cx="276" cy="277" rx="232" ry="266" filter="url(#page-shadow)"/>

    <text class="page-title" x="290" y="92" text-anchor="middle">Lighting &amp; Decor</text>

    <g class="body-copy" text-anchor="middle">
      <text x="293" y="152">Let our experts draw attention to your carefully chosen</text>
      <text x="293" y="165.5">centerpieces, surround your guests with your event colors and</text>
      <text x="293" y="179">even write your initials in light. Looking for something romantic?</text>
      <text x="293" y="192.5">Imagine dining under lanterns and chandeliers. Ready to transform your</text>
      <text x="293" y="206">event to a hot dance club? Let our experts swirl and strobe light over your</text>
      <text x="293" y="219.5">guests and dancefloor.</text>
      <text x="293" y="246">We offer a wide range of lighting services including, but not limited to:</text>
    </g>

    <g class="service-list">
      <g class="service-column">
        <circle class="bullet" cx="172" cy="263" r="2"/><text x="182" y="266.5">Pinspots</text>
        <circle class="bullet" cx="172" cy="276.5" r="2"/><text x="182" y="280">Intelligent Lighting</text>
        <circle class="bullet" cx="172" cy="290" r="2"/><text x="182" y="293.5">Uplighting</text>
        <circle class="bullet" cx="172" cy="303.5" r="2"/><text x="182" y="307">Special FX</text>
        <circle class="bullet" cx="172" cy="317" r="2"/><text x="182" y="320.5">Dance Floors</text>
        <circle class="bullet" cx="172" cy="330.5" r="2"/><text x="182" y="334">Draping</text>
        <circle class="bullet" cx="172" cy="344" r="2"/><text x="182" y="347.5">Cafe Lights</text>
      </g>
      <g class="service-column">
        <circle class="bullet" cx="323" cy="263" r="2"/><text x="333" y="266.5">Staging</text>
        <circle class="bullet" cx="323" cy="276.5" r="2"/><text x="333" y="280">Search Lights</text>
        <circle class="bullet" cx="323" cy="290" r="2"/><text x="333" y="293.5">Vinyl</text>
        <circle class="bullet" cx="323" cy="303.5" r="2"/><text x="333" y="307">Video Projection</text>
        <circle class="bullet" cx="323" cy="317" r="2"/><text x="333" y="320.5">Monograms</text>
        <circle class="bullet" cx="323" cy="330.5" r="2"/><text x="333" y="334">Chiavari Chairs</text>
        <circle class="bullet" cx="323" cy="344" r="2"/><text x="333" y="347.5">Custom Designs</text>
      </g>
    </g>

    <g class="photo-group" clip-path="url(#left-page-clip)">
      <g class="photo" role="img" aria-label="Photo: venue entrance with chandelier and lit monogram">
        <circle cx="112" cy="395" r="64" fill="url(#tone-monogram-venue)"/>
        <circle class="frame-plum" cx="112" cy="395" r="64"/>
      </g>
      <g class="photo" role="img" aria-label="Photo: tent reception washed in blue and purple gobo lighting">
        <circle cx="330" cy="470" r="104" fill="url(#tone-tent-gobo)"/>
        <circle class="frame-gold" cx="330" cy="470" r="104"/>
      </g>
    </g>
  </g>

  <!-- Right page -->
  <g class="page page-right">
    <ellipse class="page-shape" cx="737" cy="277" rx="240" ry="268" filter="url(#page-shadow)"/>

    <g class="photo-group" clip-path="url(#right-page-clip)">
      <g class="photo" role="img" aria-label="Photo: arched hall with chandeliers, teal uplighting and ceremony chairs">
        <circle cx="655" cy="118" r="118" fill="url(#tone-chandelier-hall)"/>
        <circle class="frame-plum" cx="655" cy="118" r="118"/>
      </g>
      <g class="photo" role="img" aria-label="Photo: candlelit table with pink floral centerpiece">
        <circle cx="862" cy="102" r="76" fill="url(#tone-candle-table)"/>
        <circle class="frame-gold" cx="862" cy="102" r="76"/>
      </g>
      <g class="photo" role="img" aria-label="Photo: search light beams in the night sky">
        <circle cx="555" cy="296" r="68" fill="url(#tone-searchlight)"/>
        <circle class="frame-plum" cx="555" cy="296" r="68"/>
      </g>
      <g class="photo" role="img" aria-label="Photo: tiered dessert display against white draping">
        <circle cx="744" cy="334" r="82" fill="url(#tone-dessert-display)"/>
        <circle class="frame-plum" cx="744" cy="334" r="82"/>
      </g>
      <g class="photo" role="img" aria-label="Photo: reception hall with purple lighting and patterned ceiling">
        <circle cx="893" cy="320" r="80" fill="url(#tone-purple-hall)"/>
        <circle class="frame-plum" cx="893" cy="320" r="80"/>
      </g>
      <g class="photo" role="img" aria-label="Photo: table with white centerpiece under snowflake projections">
        <circle cx="668" cy="454" r="94" fill="url(#tone-snowflake-room)"/>
        <circle class="frame-gold" cx="668" cy="454" r="94"/>
      </g>
    </g>
  </g>

  <line class="fold-line" x1="500" y1="128" x2="500" y2="512"/>
</svg>
</body>
</html>
```